Menu Design marlowe

I need to create a take out menu for my restaurant something nice with some pictures. clean and simple with the colors of my reatsurant. which are orange and black. mostly black.

its fairly simple it has to be 4 pages front cover, inside front menu then 2nd page front and back with menu then 3rd page back front menu, back 3rd sushi menu with specials. final page 4th page, back map with adress and opening hours. and back cover final.

simple elegant and class. black and orange i will send logo and menu as well and pictures.

i am a high end bistro that serves gourmet pizza and pasta. we also have a sushi bar.
the menu will be 6 inches width by 9 inches

the menu that i sent is a pdf file. had an error with word please change font and make a new word dosument.

thank you

Industry/Entity Type

Restaurant

Requirements
Must have
• the colors which are black and orange. mostly black.

```html
<!DOCTYPE html>
<html lang="fr">
<head>
<meta charset="utf-8">
<title>Marlowe – Menu Pizza</title>
<link rel="stylesheet" href="https://fonts.googleapis.com/css2?family=Indie+Flower&family=Didact+Gothic&display=swap">
<style>
  :root {
    --canvas: #ffffff;
    --orange: #f7941d;
    --ink: #1a1a1a;
    --panel: rgba(28, 28, 28, 0.86);
    --photo-light: #d9d9d9;
    --photo-mid: #8a8a8a;
    --photo-dark: #2e2e2e;
    --logo-faint: rgba(255, 255, 255, 0.28);
    --logo-faint-dark: rgba(120, 120, 120, 0.35);
  }
  * { box-sizing: border-box; margin: 0; padding: 0; }
  html, body {
    width: 1200px; height: 900px; overflow: hidden;
    background: var(--canvas);
  }
  .spread {
    position: absolute; left: 93px; top: 70px;
    width: 1014px; height: 760px;
    display: flex;
    box-shadow: 0 6px 24px rgba(0,0,0,0.18);
  }
  .page { position: relative; width: 507px; height: 760px; overflow: hidden; }

  .photo { position: absolute; inset: 0; }
  .photo--counter {
    background:
      radial-gradient(ellipse at 30% 35%, var(--photo-light) 0%, transparent 55%),
      linear-gradient(180deg, #c8c8c8 0%, var(--photo-mid) 45%, #5a5a5a 75%, #3a3a3a 100%);
  }
  .photo--dining {
    background:
      radial-gradient(ellipse at 70% 30%, #b5b5b5 0%, transparent 50%),
      linear-gradient(180deg, #a8a8a8 0%, #6e6e6e 50%, var(--photo-dark) 100%);
  }

  .brand {
    position: absolute;
    font-family: "Indie Flower", cursive;
    font-size: 54px; letter-spacing: 1px;
    color: var(--logo-faint-dark);
  }
  .brand--cover { left: 150px; top: 60px; }

  .menu-panel {
    position: absolute; left: 50px; top: 0;
    width: 405px; height: 760px;
    background: var(--panel);
  }
  .menu-title {
    margin-top: 10px;
    height: 34px; line-height: 34px;
    background: var(--orange);
    color: var(--ink);
    text-align: center;
    font-family: "Didact Gothic", sans-serif;
    font-size: 17px; letter-spacing: 1px;
  }
  .menu-list {
    list-style: none;
    padding: 18px 22px 0 18px;
    font-family: "Indie Flower", cursive;
    font-size: 10.5px; line-height: 13px;
    text-transform: uppercase;
    color: var(--orange);
  }
  .dish { margin-bottom: 11px; }
  .dish__head { display: flex; justify-content: space-between; }
  .dish__price { white-space: nowrap; padding-left: 10px; }

  .menu-notes {
    padding: 6px 22px 0 18px;
    font-family: "Indie Flower", cursive;
    font-size: 10.5px; line-height: 13px;
    text-transform: uppercase;
    color: var(--orange);
  }
  .note { display: flex; justify-content: space-between; }

  .brand--panel {
    left: 80px; bottom: 20px;
    color: var(--logo-faint);
  }
</style>
</head>
<body>
  <main class="spread">
    <section class="page page--cover">
      <div class="photo photo--counter" role="img" aria-label="Black and white photo of the bistro counter with menus and a cashier"></div>
      <div class="brand brand--cover">marlowe</div>
    </section>

    <section class="page page--pizza">
      <div class="photo photo--dining" role="img" aria-label="Black and white photo of the dining room with waiters and tables"></div>
      <div class="menu-panel">
        <h1 class="menu-title">PIZZA</h1>
        <ul class="menu-list">
          <li class="dish"><div class="dish__head"><span>Margarita</span><span class="dish__price">$15.50</span></div>
            <div>Sauce tomate, mozzarella &amp; basilic</div><div>Tomato sauce, mozzarella &amp; basil</div></li>
          <li class="dish"><div class="dish__head"><span>Champignon</span><span class="dish__price">$17.50</span></div>
            <div>Champignon, sauce tomate, mozzarella</div><div>Mushrooms, tomato sauce, mozzarella</div></li>
          <li class="dish"><div class="dish__head"><span>Trilogie d'olive / Olive trilogy</span><span class="dish__price">$17.50</span></div>
            <div>Olives, sauce tomate piquante &amp; mozzarella</div><div>Olives, spicy tomato sauce &amp; mozzarella</div></li>
          <li class="dish"><div class="dish__head"><span>Végétarienne / Vegetarian</span><span class="dish__price">$18.50</span></div>
            <div>Légumes grillés, sauce tomate &amp; mozzarella</div><div>Grilled veggies, tomato sauce, mozzarella</div></li>
          <li class="dish"><div class="dish__head"><span>Pizza Marlowe / Marlowe pizza</span><span class="dish__price">$18.50</span></div>
            <div>Tomates séchées, aubergine, olives, sauce tomate &amp; mozzarella</div><div>Sun dried tomatoes, eggplant, olives, tomato sauce &amp; mozzarella</div></li>
          <li class="dish"><div class="dish__head"><span>Grecque / Greek</span><span class="dish__price">$19.00</span></div>
            <div>Feta, olives, oignons rouges, mozzarella, sauce tomate</div><div>Feta, olives, red onions, mozzarella, tomato sauce</div></li>
          <li class="dish"><div class="dish__head"><span>Thon / Tuna</span><span class="dish__price">$18.50</span></div>
            <div>Thon, olives, sauce tomate &amp; mozzarella</div><div>Tuna, olives, tomato sauce &amp; mozzarella</div></li>
          <li class="dish"><div class="dish__head"><span>Niçoise</span><span class="dish__price">$19.00</span></div>
            <div>Anchois, olives, sauce tomate &amp; mozzarella</div><div>Anchovies, olives, mozzarella &amp; tomato sauce</div></li>
          <li class="dish"><div class="dish__head"><span>Fruit de mer / Seafood</span><span class="dish__price">$19.00</span></div>
            <div>Crevettes, poireaux, sauce tomate &amp; mozzarella</div><div>Shrimp, leeks, tomato sauce &amp; mozzarella</div></li>
          <li class="dish"><div class="dish__head"><span>Calzone</span><span class="dish__price">$18.50</span></div>
            <div>Poivron rouge, vert &amp; jaune, champignons, oignons, sauce tomate &amp; mozzarella</div><div>Red, yellow &amp; green peppers, mushrooms, onions, tomato sauce &amp; mozzarella</div></li>
        </ul>
        <div class="menu-notes">
          <div>Toutes nos pizzas sont disponibles sans fromage</div>
          <div>All our pizzas are available without cheese</div>
          <div class="note"><span>Ajoutez deux œufs / Add two eggs</span><span class="dish__price">$1.95</span></div>
          <div class="note"><span>Pâte blé entier</span><span class="dish__price">$1.25</span></div>
        </div>
        <div class="brand brand--panel">marlowe</div>
      </div>
    </section>
  </main>
</body>
</html>
```